Florida-based Coastal Landscaping Comapny Needs Postcard Designs

We are a newly established Florida-based, coastal landscaping company that is looking for some really innovative postcards that we can use to get our name our to affluent consumers that live on the coast of Florida (think on the beach) and small to medium sized businesses in the same area. We will be sending out 100s of thousands of these, so need a great design

Target Market(s)

Affluent consumers and small to medium sized businesses

Industry/Entity Type

Landscaping

Font styles to use
Sans Serif

Colors

Designer to choose colors to be used in the design.

Requirements
Must have
• Florida - looking, island looking / paradise, but incorporate landscaping themes
• Need to say something about "Enjoy your yard this summer" or something relating to summer, landscapes and florida
• and would like to make two offers $50.00 off with signing up for one of our routine maintenance programs, or 1 free landscape inspection
Should not have
• Regular generic lawn company designs. We are a top tier landscape design / build plus maintenance firm, so not your mom and pop lawn mowing company

```html
<!DOCTYPE html>
<html lang="en">
<head>
<meta charset="utf-8">
<title>Shorewell Postcard</title>
<link rel="stylesheet" href="https://fonts.googleapis.com/css2?family=Cinzel:wght@600;700&family=Lato:wght@400;700&family=Oswald:wght@600&display=swap">
<style>
  :root {
    --page-bg: #2e2e2e;
    --card-white: #ffffff;
    --ink-dark: #1c1c1c;
    --brand-teal: #1e9cc6;
    --sky-top: #d3e8f8;
    --sky-bottom: #4f94d6;
    --photo-blue: #5d9ad6;
    --photo-green: #7db53a;
    --lawn-light: #8fc63a;
    --lawn-dark: #3f8a1f;
    --badge-green: #7cbf2e;
    --line-grey: #8a8a8a;
  }
  * { box-sizing: border-box; margin: 0; padding: 0; }
  html, body { width: 902px; height: 1200px; overflow: hidden; background: var(--page-bg); }
  .canvas { position: relative; width: 902px; height: 1200px; }
  .postcard { position: absolute; left: 121px; width: 660px; height: 500px; box-shadow: 0 6px 18px rgba(0,0,0,.45); }
  .postcard--front { top: 70px; }
  .postcard--back { top: 630px; }
  .postcard svg { display: block; width: 660px; height: 500px; }
  .brand-name { font-family: "Cinzel", serif; font-weight: 700; fill: var(--brand-teal); letter-spacing: 1px; }
  .headline { font-family: "Cinzel", serif; font-weight: 700; fill: var(--ink-dark); font-size: 42px; }
  .badge-price { font-family: "Oswald", sans-serif; font-weight: 600; fill: var(--ink-dark); }
  .badge-note { font-family: "Lato", sans-serif; font-weight: 700; fill: #ffffff; }
  .intro-text { font-family: "Lato", sans-serif; font-weight: 700; fill: #ffffff; font-size: 15px; }
  .call-label { font-family: "Lato", sans-serif; font-weight: 700; fill: #ffffff; font-size: 16px; }
  .call-number { font-family: "Lato", sans-serif; font-weight: 700; fill: #ffffff; font-size: 24px; }
</style>
</head>
<body>
<main class="canvas">

  <section class="postcard postcard--front">
    <svg viewBox="0 0 660 500" xmlns="http://www.w3.org/2000/svg">
      <defs>
        <linearGradient id="paper" x1="0" y1="0" x2="1" y2="1">
          <stop offset="0" stop-color="#ffffff"/><stop offset="1" stop-color="#e2e2e2"/>
        </linearGradient>
        <linearGradient id="skySoft" x1="0" y1="0" x2="0" y2="1">
          <stop offset="0" stop-color="var(--sky-top)"/><stop offset="1" stop-color="var(--sky-bottom)"/>
        </linearGradient>
        <linearGradient id="lawnSoft" x1="0" y1="0" x2="0" y2="1">
          <stop offset="0" stop-color="var(--lawn-light)"/><stop offset="1" stop-color="var(--lawn-dark)"/>
        </linearGradient>
        <linearGradient id="photoSoft" x1="0" y1="0" x2="0" y2="1">
          <stop offset="0" stop-color="var(--photo-blue)"/><stop offset="1" stop-color="var(--photo-green)"/>
        </linearGradient>
        <radialGradient id="badgeFill" cx="0.5" cy="0.35" r="0.7">
          <stop offset="0" stop-color="#b6dc4a"/><stop offset="0.6" stop-color="#7cbf2e"/>
          <stop offset="1" stop-color="#3f8a1f"/>
        </radialGradient>
        <clipPath id="frontCard"><rect width="660" height="500"/></clipPath>
      </defs>
      <g clip-path="url(#frontCard)">
        <rect width="660" height="500" fill="url(#paper)"/>
        <path d="M0 182 C 110 150, 230 160, 320 230 L 660 360 L 660 500 L 0 500 Z" fill="var(--ink-dark)"/>
        <path role="img" aria-label="Bright summer sky with sunshine" d="M0 190 C 110 158, 230 168, 320 238 L 660 368 L 660 500 L 0 500 Z" fill="url(#skySoft)"/>
        <path role="img" aria-label="Green grass" d="M0 478 C 200 450, 420 432, 660 425 L 660 500 L 0 500 Z" fill="url(#lawnSoft)"/>

        <circle cx="545" cy="55" r="292" fill="var(--badge-green)"/>
        <circle cx="512" cy="78" r="272" fill="var(--brand-teal)"/>
        <circle cx="512" cy="78" r="266" fill="#ffffff"/>
        <circle role="img" aria-label="Coastal garden with palm trees, hedges and sea view" cx="515" cy="78" r="258" fill="url(#photoSoft)"/>

        <text class="brand-name" x="28" y="112" font-size="30">SHOREWELL</text>

        <text class="headline" x="72" y="312">Enjoy</text>
        <text class="headline" x="72" y="366">your yard</text>
        <text class="headline" x="72" y="420">this summer</text>

        <circle cx="500" cy="345" r="80" fill="#ffffff"/>
        <circle cx="500" cy="345" r="74" fill="url(#badgeFill)"/>
        <circle cx="500" cy="345" r="77" fill="none" stroke="#555" stroke-width="1" stroke-dasharray="3 3"/>
        <text class="badge-price" x="482" y="342" font-size="32" text-anchor="middle">$50.00</text>
        <text class="badge-price" transform="translate(548 343) rotate(-90)" font-size="16">OFF</text>
        <text class="badge-note" x="500" y="365" font-size="10" text-anchor="middle">with signing up for one of</text>
        <text class="badge-note" x="500" y="378" font-size="10" text-anchor="middle">our routine maintenance</text>
        <text class="badge-note" x="500" y="391" font-size="10" text-anchor="middle">programs</text>
      </g>
    </svg>
  </section>

  <section class="postcard postcard--back">
    <svg viewBox="0 0 660 500" xmlns="http://www.w3.org/2000/svg">
      <defs>
        <linearGradient id="photoSoftBack" x1="0" y1="0" x2="0" y2="1">
          <stop offset="0" stop-color="var(--photo-blue)"/><stop offset="1" stop-color="var(--photo-green)"/>
        </linearGradient>
        <linearGradient id="lawnBack" x1="0" y1="0" x2="0" y2="1">
          <stop offset="0" stop-color="#6fb036"/><stop offset="1" stop-color="var(--lawn-dark)"/>
        </linearGradient>
        <radialGradient id="badgeFillBack" cx="0.5" cy="0.35" r="0.7">
          <stop offset="0" stop-color="#b6dc4a"/><stop offset="0.6" stop-color="#7cbf2e"/>
          <stop offset="1" stop-color="#3f8a1f"/>
        </radialGradient>
        <clipPath id="photoArea"><path d="M0 0 L 330 0 C 400 120, 390 300, 270 420 L 0 420 Z"/></clipPath>
      </defs>
      <rect width="660" height="500" fill="#ffffff"/>
      <path d="M300 0 L 350 0 C 420 130, 400 300, 305 420 L 270 420 C 380 300, 395 130, 300 0 Z" fill="var(--ink-dark)"/>
      <path d="M330 150 C 345 260, 320 350, 265 420 L 300 420 C 355 350, 365 260, 345 150 Z" fill="var(--brand-teal)"/>
      <g clip-path="url(#photoArea)">
        <rect role="img" aria-label="Tropical beach with palm tree and lounge chairs" width="400" height="260" fill="url(#photoSoftBack)"/>
        <path d="M0 250 C 120 270, 260 230, 400 160 L 400 420 L 0 420 Z" fill="url(#lawnBack)"/>
      </g>

      <circle cx="80" cy="190" r="68" fill="#ffffff"/>
      <circle cx="80" cy="190" r="62" fill="url(#badgeFillBack)"/>
      <circle cx="80" cy="190" r="65" fill="none" stroke="#555" stroke-width="1" stroke-dasharray="3 3"/>
      <text class="badge-price" x="64" y="190" font-size="27" text-anchor="middle">$50.00</text>
      <text class="badge-price" transform="translate(121 191) rotate(-90)" font-size="13">OFF</text>
      <text class="badge-note" x="80" y="208" font-size="8.5" text-anchor="middle">with signing up for one of</text>
      <text class="badge-note" x="80" y="219" font-size="8.5" text-anchor="middle">our routine maintenance</text>
      <text class="badge-note" x="80" y="230" font-size="8.5" text-anchor="middle">programs</text>

      <g transform="rotate(-4 50 310)">
        <text class="intro-text" x="45" y="312">We are a newly established Florida-based,</text>
        <text class="intro-text" x="45" y="332">coastal landscaping company</text>
        <text class="call-label" x="50" y="380">Call Us:</text>
        <text class="call-number" x="118" y="382">5550142890</text>
      </g>

      <text class="brand-name" x="378" y="52" font-size="18">SHOREWELL</text>
      <rect x="545" y="30" width="58" height="64" fill="none" stroke="#555" stroke-width="1"/>
      <line x1="405" y1="232" x2="610" y2="218" stroke="var(--line-grey)" stroke-width="1"/>
      <line x1="408" y1="272" x2="612" y2="258" stroke="var(--line-grey)" stroke-width="1"/>
      <line x1="411" y1="312" x2="615" y2="298" stroke="var(--line-grey)" stroke-width="1"/>
    </svg>
  </section>

</main>
</body>
</html>
```